Southland Rig Academy needs a modern website that oozes professionalism

Our current website is boring and looks like everyone elses. We need a modern website that says we are the best at plant operator training. We use Ironvale and Darvento equipment for our training. We train all over Australia in Civil Construction, Mining and Quarrying. We want to be the "Go to" website for all plant operator training in Australia.

Industry/Entity Type

Heavy Machinery Training

Colors
0054AA
0677BA
7BADD7
CADEEF
E8F1F8
FFF300
FFF600
FEFA6F
FFFEC7
FFFEE8

```html
<!DOCTYPE html>
<html lang="en">
<head>
<meta charset="utf-8">
<title>Southland Rig Academy</title>
<link href="https://fonts.googleapis.com/css2?family=Oswald:wght@500;600&family=Outfit:wght@300;400;500;600&display=swap" rel="stylesheet">
<style>
:root{
  --navy:#1d2a7e;
  --navy-dark:#16205f;
  --yellow:#fbb900;
  --ink:#1a1a1a;
  --body:#3a3a3a;
  --muted:#8a8a8a;
  --footer:#1f1f1f;
  --footer-text:#d8d8d8;
  --white:#ffffff;
}
*{box-sizing:border-box;margin:0;padding:0}
html,body{width:1200px;height:3856px;overflow:hidden}
body{font-family:'Outfit',sans-serif;color:var(--body);background:var(--white);position:relative}
.abs{position:absolute}
.heading{position:absolute;left:0;width:1200px;font-family:'Oswald',sans-serif;font-weight:600;color:var(--ink);text-transform:uppercase;text-align:center;font-size:40px;line-height:50px;letter-spacing:.3px}
.rule{width:64px;height:3px;background:var(--yellow);position:absolute;left:568px}
.btn{position:absolute;background:var(--yellow);color:var(--ink);border-radius:20px;font-size:13px;font-weight:500;display:flex;align-items:center;justify-content:center;text-transform:uppercase;letter-spacing:.3px}

/* hero */
.hero{position:absolute;left:0;top:0;width:1200px;height:624px;background:linear-gradient(100deg,#55606a 0%,#8c8f8a 30%,#b7a24a 48%,#d9792f 70%,#5a5650 100%)}
.topbar{position:absolute;left:568px;top:0;width:545px;height:33px;background:var(--navy-dark);display:flex;align-items:center;padding-left:22px;font-size:15px;font-weight:500}
.topbar .phone{color:var(--white);display:flex;align-items:center;gap:6px}
.topbar .sep{width:1px;height:20px;background:#6670b0;margin:0 10px}
.topbar .hl{color:var(--yellow)}
.topbar .social{display:flex;gap:9px;margin-left:4px}
.topbar .social span{width:11px;height:11px;background:var(--white);border-radius:2px}
.brand{position:absolute;display:flex;align-items:center;gap:12px;color:var(--white);font-weight:600;text-transform:uppercase;letter-spacing:.5px}
.brand .mark{border-radius:50%;border:3px solid var(--white)}
.nav{position:absolute;top:55px;left:396px;display:flex;gap:28px;color:var(--white);font-size:13.5px}
.hero-title{position:absolute;left:100px;top:262px;font-family:'Oswald',sans-serif;font-weight:500;font-size:40px;line-height:46px;color:var(--white);text-transform:uppercase}

/* cards */
.cards{position:absolute;left:100px;width:1000px;display:flex;gap:20px}
.card{width:235px;height:292px;background:var(--white);box-shadow:0 1px 6px rgba(0,0,0,.12);text-align:center}
.card .ph{height:151px;border-bottom:3px solid var(--yellow)}
.card h3{font-size:14px;font-weight:500;color:var(--ink);margin-top:14px}
.card p{font-size:11.5px;line-height:19px;color:var(--body);padding:6px 17px 0;text-align:justify;text-align-last:center}
.card a{display:inline-block;margin-top:6px;font-size:13px;font-weight:600;color:var(--navy);text-decoration:underline;text-underline-offset:3px}

/* about */
.about-band{position:absolute;left:0;top:1144px;width:1200px;height:472px;background:linear-gradient(90deg,#b08a2a 0%,#8a6a25 28%,#6a6a6e 50%,#4e5160 75%,#3e4252 100%)}
.about-title{position:absolute;left:655px;top:1212px;font-family:'Oswald',sans-serif;font-weight:500;font-size:40px;line-height:50px;color:var(--white)}
.about-rule{position:absolute;left:655px;top:1269px;width:62px;height:3px;background:var(--yellow)}
.about-text{position:absolute;left:655px;top:1293px;width:444px;color:var(--white);font-size:11.6px;line-height:19px;text-align:justify}
.about-text p+p{margin-top:9px}

/* why */
.why-intro{position:absolute;left:140px;top:1758px;width:920px;text-align:center;font-size:14px;line-height:23px}
.feature{position:absolute;width:290px;text-align:center}
.feature .ic{width:98px;height:98px;border-radius:50%;background:var(--yellow);margin:0 auto;display:flex;align-items:center;justify-content:center}
.feature h4{font-size:19px;font-weight:600;color:var(--ink);margin-top:26px;text-transform:uppercase}
.feature p{font-size:13.5px;line-height:23px;margin-top:8px;padding:0 20px}

/* partner */
.partner-band{position:absolute;left:0;top:2118px;width:1200px;height:332px;background:linear-gradient(90deg,#22307f 0%,#1d2a7e 50%,#243393 100%)}
.partner-text{position:absolute;left:180px;top:2260px;width:840px;text-align:center;color:var(--white);font-size:16px;line-height:27px;font-weight:500}

/* contact */
.contact-ph{position:absolute;left:0;top:2988px;width:598px;height:538px;background:linear-gradient(120deg,#6b4a30 0%,#c99a2a 45%,#e6b528 65%,#8a6e3a 100%)}
.contact-title{position:absolute;left:640px;top:3048px;font-family:'Outfit',sans-serif;font-weight:500;font-size:31px;line-height:40px;color:var(--ink);letter-spacing:.8px;text-transform:uppercase}
.contact-sub{position:absolute;left:640px;top:3132px;font-size:17px;color:var(--body);letter-spacing:.3px}
.field{position:absolute;border:1px solid #c9c9c9;border-radius:3px;font-size:13px;color:var(--muted);padding:10px 13px}

/* footer */
.footer{position:absolute;left:0;top:3526px;width:1200px;height:330px;background:var(--footer);color:var(--footer-text)}
.footer-col{position:absolute;top:59px}
.footer-col h5{font-size:19px;font-weight:500;color:var(--white);margin-bottom:12px}
.footer-col li{list-style:none;font-size:13.5px;line-height:30.5px;font-weight:300}
.footer-col .info{font-size:13.5px;line-height:20px;font-weight:300}
.footer-social{position:absolute;top:147px;width:38px;height:38px;border-radius:50%;background:var(--white)}
.footer-divider{position:absolute;left:100px;top:274px;width:1000px;height:1px;background:#5a5a5a}
.footer-copy{position:absolute;left:0;top:289px;width:1200px;text-align:center;font-size:14px;font-weight:300}
</style>
</head>
<body>

<!-- Hero -->
<section class="hero" role="img" aria-label="Photo of two plant operator trainees in hi-vis vests and hard hats reviewing a clipboard beside heavy machinery"></section>
<div class="topbar">
  <span class="phone"><svg width="13" height="13" viewBox="0 0 24 24"><path fill="#fff" d="M6.6 10.8a15.1 15.1 0 006.6 6.6l2.2-2.2c.3-.3.7-.4 1-.2 1.1.4 2.3.6 3.6.6.6 0 1 .4 1 1V20c0 .6-.4 1-1 1A17 17 0 013 4c0-.6.4-1 1-1h3.5c.6 0 1 .4 1 1 0 1.3.2 2.5.6 3.6.1.3 0 .7-.2 1z"/></svg>1300 - 622 - 418</span>
  <span class="sep"></span><span class="hl">Course Calendar</span>
  <span class="sep"></span><span class="hl">Student Handbook</span>
  <span class="sep"></span>
  <span class="social"><span></span><span></span><span></span></span>
</div>
<div class="brand" style="left:100px;top:12px;font-size:19px;">
  <span class="mark" style="width:54px;height:54px;"></span>
  <span style="line-height:20px;border-bottom:2px solid #fff;padding-bottom:4px">Southland<br>Rig Academy</span>
</div>
<nav class="nav"><span>About</span><span>Courses</span><span>Onsite / Private Courses</span><span>Online Training</span><span>Our Services</span><span>Student Information</span></nav>
<h1 class="hero-title">Training and experience<br>you can rely on</h1>
<div class="btn" style="left:100px;top:378px;width:144px;height:36px;">Get Started</div>

<!-- Our Courses -->
<h2 class="heading" style="top:683px;">Our Courses</h2>
<div class="rule" style="top:738px"></div>
<div class="cards" style="top:773px">
  <div class="card"><div class="ph" role="img" aria-label="Photo of a worker holding a white hard hat at sunset" style="background:linear-gradient(120deg,#e9d27a,#c9c3b5 50%,#e06a2a)"></div><h3>Full Qualifications</h3><p>Operating heavy machinery is a specialized skill in construction and mining. Those who are looking</p><a>LEARN MORE</a></div>
  <div class="card"><div class="ph" role="img" aria-label="Photo of a yellow haul truck in a quarry" style="background:linear-gradient(120deg,#5a5a5a,#c49a28 55%,#3e3e3e)"></div><h3>High Risk Licencing</h3><p>Operating heavy machinery is a specialized skill in construction and mining. Those who are looking</p><a>LEARN MORE</a></div>
  <div class="card"><div class="ph" role="img" aria-label="Photo of an operator in a hi-vis vest and safety harness" style="background:linear-gradient(120deg,#e8d9a8,#e07a2a 55%,#7a8a9a)"></div><h3>Plant Operator Tickets</h3><p>Operating heavy machinery is a specialized skill in construction and mining. Those who are looking</p><a>LEARN MORE</a></div>
  <div class="card"><div class="ph" role="img" aria-label="Photo of two technicians in hard hats inspecting equipment" style="background:linear-gradient(120deg,#7a6a55,#bca98a 50%,#4a4440)"></div><h3>Short Courses</h3><p>Operating heavy machinery is a specialized skill in construction and mining. Those who are looking</p><a>LEARN MORE</a></div>
</div>

<!-- About -->
<section class="about-band" role="img" aria-label="Photo of large yellow mining haul trucks lined up under a cloudy sky"></section>
<h2 class="about-title">ABOUT US</h2>
<div class="about-rule"></div>
<div class="about-text">
  <p>Southland Rig Academy is a versatile team of passionate Health, Safety and Training professionals, all striving towards the common goal of achieving no harm to people, assets and the environment. Our experienced team have been servicing the Bowen Basin mining industry for over 10 years and we have trainers based throughout Queensland.</p>
  <p>During this time we have established a solid reputation for delivering thorough, timely, and efficient services that are specifically tailored to meet the individual needs of our valued clients within the Mining, Oil &amp; Gas, Civil, Construction, Manufacturing and Agricultural sectors.</p>
</div>
<div class="btn" style="left:652px;top:1499px;width:143px;height:36px;">Learn More</div>

<!-- Why choose us -->
<h2 class="heading" style="top:1680px;">Why choose us?</h2>
<div class="rule" style="top:1733px"></div>
<p class="why-intro">Southland Rig Academy consultants have come from the same industries that we consult back to. Our wealth of first hand knowledge and experience enables us to make invaluable contributions to all facets of safety and training in your workplace.</p>
<div class="feature" style="left:103px;top:1839px">
  <div class="ic"><svg width="50" height="50" viewBox="0 0 50 50" fill="none" stroke="#1a1a1a" stroke-width="2"><path d="M14 18a11 11 0 0122 0z"/><circle cx="25" cy="23" r="6"/><path d="M10 44c0-9 6-13 15-13s15 4 15 13z"/><path d="M32 34l6-2 6 2v5c0 4-3 6-6 7-3-1-6-3-6-7z" fill="#fbb900"/></svg></div>
  <h4>We are passionate</h4><p>We are passionate about Health and Safety.</p>
</div>
<div class="feature" style="left:455px;top:1839px">
  <div class="ic"><svg width="52" height="52" viewBox="0 0 52 52" fill="none" stroke="#1a1a1a" stroke-width="2"><circle cx="26" cy="12" r="6"/><path d="M6 28l10-6 8 4 6-3 16 6"/><path d="M12 32l10 10c2 2 4 2 6 0l12-10"/><path d="M20 30l8 6M24 28l8 6"/></svg></div>
  <h4>We are dependable</h4><p>Let us deliver the right training solution for your business.</p>
</div>
<div class="feature" style="left:805px;top:1839px">
  <div class="ic"><svg width="50" height="50" viewBox="0 0 50 50" fill="none" stroke="#1a1a1a" stroke-width="2"><rect x="18" y="8" width="26" height="20"/><path d="M22 14h18M22 19h12M22 24h8"/><circle cx="11" cy="16" r="4"/><path d="M5 38V26c0-3 3-5 6-5s5 2 7 4l6-2"/><path d="M31 28l-4 14M31 28l4 14"/></svg></div>
  <h4>Nationally recognised</h4><p>We are accredited to delivery nationally recognised training.</p>
</div>

<!-- Trusted partner -->
<section class="partner-band" role="img" aria-label="Navy-tinted photo of an excavator working on a mine site"></section>
<h2 class="heading" style="top:2181px;color:#fff;">Your trusted training partner</h2>
<div class="rule" style="top:2237px"></div>
<p class="partner-text">We assist our clients in their ongoing quest to achieve zero harm by providing them with the highest calibre of health and safety management advice and personalised training.</p>
<div class="btn" style="left:528px;top:2343px;width:144px;height:35px;">Contact Us</div>

<!-- Our Courses 2 -->
<h2 class="heading" style="top:2521px;">Our Courses</h2>
<div class="rule" style="top:2576px"></div>
<div class="cards" style="top:2610px">
  <div class="card"><div class="ph" role="img" aria-label="Photo of two workers in orange overalls on a mine site" style="background:linear-gradient(120deg,#9aa6b0,#d27a2a 55%,#7a6a55)"></div><h3>ONLINE REFRESHER COURSES</h3><p>Operating heavy machinery is a specialized skill in construction and mining. Those who are looking</p><a>LEARN MORE</a></div>
  <div class="card"><div class="ph" role="img" aria-label="Photo of a haul truck being loaded with rock" style="background:linear-gradient(120deg,#8a8a8a,#5a5a5a 55%,#a8a8a8)"></div><h3>EXPRESS COURSES</h3><p>Operating heavy machinery is a specialized skill in construction and mining. Those who are looking</p><a>LEARN MORE</a></div>
  <div class="card"><div class="ph" role="img" aria-label="Photo of workers reviewing documents beside a forklift" style="background:linear-gradient(120deg,#5a7ab0,#e6c23a 55%,#9aa0aa)"></div><h3>FREE COURSES</h3><p>Operating heavy machinery is a specialized skill in construction and mining. Those who are looking</p><a>LEARN MORE</a></div>
  <div class="card"><div class="ph" role="img" aria-label="Photo of two workers in orange overalls crouched by an excavator" style="background:linear-gradient(120deg,#8a8a82,#e06a2a 55%,#5a5248)"></div><h3>Plant Operator Tickets</h3><p>Operating heavy machinery is a specialized skill in construction and mining. Those who are looking</p><a>LEARN MORE</a></div>
</div>

<!-- Contact -->
<div class="contact-ph" role="img" aria-label="Photo of two workers in hard hats inspecting a large yellow machine wheel"></div>
<h2 class="contact-title">Do you want to inquire<br>about a coaching service?</h2>
<p class="contact-sub">Send me a message here if you would like to connect!</p>
<div class="field" style="left:637px;top:3183px;width:226px;height:39px;">First Name</div>
<div class="field" style="left:871px;top:3183px;width:226px;height:39px;">Last Name</div>
<div class="field" style="left:637px;top:3234px;width:460px;height:39px;">Email</div>
<div class="field" style="left:637px;top:3285px;width:460px;height:124px;">Type your message here</div>
<div class="btn" style="left:787px;top:3433px;width:143px;height:35px;">Submit</div>

<!-- Footer -->
<footer class="footer">
  <div class="brand" style="left:130px;top:72px;font-size:17px;">
    <span class="mark" style="width:50px;height:50px;"></span>
    <span style="line-height:19px;">Southland<br>Rig Academy</span>
  </div>
  <span class="footer-social" style="left:180px"></span>
  <span class="footer-social" style="left:232px"></span>
  <span class="footer-social" style="left:285px"></span>
  <span class="footer-social" style="left:337px"></span>
  <div class="footer-col" style="left:521px"><h5>Quick Links</h5><ul><li>Home</li><li>Who We Are</li><li>Our Programs</li><li>Explore</li><li>Contact Us</li></ul></div>
  <div class="footer-col" style="left:706px"><h5>Other Links</h5><ul><li>Contact Sales</li><li>Legal Hub</li><li>Privacy Policy</li><li>Trust &amp; Security</li><li>Cookie Preferences</li></ul></div>
  <div class="footer-col" style="left:916px"><h5>Contact Info</h5>
    <p class="info">24 Harlow Road, Coalbrook,<br>Qld 4730</p>
    <p class="info" style="margin-top:10px;padding-left:4px">1300 622 418</p>
    <p class="info" style="margin-top:10px;padding-left:4px">enquiries@southlandrig.net.au</p>
  </div>
  <div class="footer-divider"></div>
  <p class="footer-copy">©Copyright 2024 Southland Rig Academy. All Rights Reserved.</p>
</footer>

</body>
</html>
```